Interior designer needs a gorgeous, chic business card design.

A new, small Interior Design firm needs a business card that is chic, contemporary and elegant. Nothing over the top. My interiors are contemporary classic with an elegant feel to them. I like to use quality finishes and products rather than follow the latest fads. Projects can be anything from Pre start selections, bathrooms, kitchens, bedrooms, custom upholstery, furniture, rugs and art etc. The final design should display quality and an achievable sense of chic. I am open to all colours including black but not limited to this.

```html
<!DOCTYPE html>
<html lang="en">
<head>
<meta charset="utf-8">
<title>Luma Interiors – Business Card</title>
<link rel="stylesheet" href="https://fonts.googleapis.com/css2?family=Questrial&display=swap">
<style>
  :root {
    --page: #ffffff;
    --slate: #6b7c86;
    --ink-light: #f2f3f4;
    --ink-soft: #dde1e3;
    --pattern-silver: #b9bfc3;
    --pattern-white: #eef0f1;
  }
  * { margin: 0; padding: 0; box-sizing: border-box; }
  html, body {
    width: 1200px;
    height: 1146px;
    overflow: hidden;
    background: var(--page);
  }
  .canvas { position: relative; width: 1200px; height: 1146px; }

  .card {
    position: absolute;
    left: 252px;
    width: 692px;
    background: var(--slate);
    color: var(--ink-light);
    overflow: hidden;
    font-family: "Questrial", sans-serif;
  }
  .card--front { top: 141px; height: 423px; }
  .card--back  { top: 578px; height: 421px; }

  .pattern-band {
    position: absolute;
    left: 0;
    width: 100%;
  }
  .pattern-band--top {
    top: 0; height: 151px;
    background: linear-gradient(to bottom, var(--pattern-silver), var(--pattern-white));
  }
  .pattern-band--bottom {
    top: 271px; height: 152px;
    background: linear-gradient(to bottom, var(--pattern-white), var(--pattern-silver));
  }
  .pattern-band--strip {
    top: 148px; height: 23px;
    background: linear-gradient(to right, var(--pattern-silver), var(--pattern-white));
  }

  .brand-name {
    position: absolute;
    left: 0;
    width: 100%;
    text-align: center;
    font-weight: 400;
    line-height: 1;
    color: var(--ink-light);
  }
  .card--front .brand-name { top: 190px; font-size: 40px; letter-spacing: 3px; }
  .card--back  .brand-name { top: 70px;  font-size: 28px; letter-spacing: 2px; }

  .contact { color: var(--ink-soft); }
  .person {
    position: absolute;
    top: 206px;
    left: 0;
    width: 100%;
    text-align: center;
    line-height: 1.15;
  }
  .person__name { font-size: 19px; }
  .person__role { font-size: 14px; }
  .contact-line {
    position: absolute;
    top: 300px;
    font-size: 14px;
  }
  .contact-line--email { left: 50px; }
  .contact-line--phone { right: 48px; }
  .contact-line--web {
    top: 362px;
    left: 0;
    width: 100%;
    text-align: center;
    font-size: 16px;
  }
</style>
</head>
<body>
<div class="canvas">

  <section class="card card--front">
    <div class="pattern-band pattern-band--top" role="img" aria-label="Decorative band of interlocking circle pattern in silver and white"></div>
    <p class="brand-name">Luma Interiors</p>
    <div class="pattern-band pattern-band--bottom" role="img" aria-label="Decorative band of interlocking circle pattern in white and silver"></div>
  </section>

  <section class="card card--back">
    <p class="brand-name">Luma Interiors</p>
    <div class="pattern-band pattern-band--strip" role="img" aria-label="Thin strip of interlocking circle pattern fading from silver to white"></div>

    <div class="contact person">
      <p class="person__name">Corina Luma Whitfield</p>
      <p class="person__role">Dip. Int. Design</p>
      <p class="person__role">Director</p>
    </div>
    <p class="contact contact-line contact-line--email">corina@lumainteriors.com.au</p>
    <p class="contact contact-line contact-line--phone">0412 555 093</p>
    <p class="contact contact-line contact-line--web">www.lumainteriors.com.au</p>
  </section>

</div>
</body>
</html>
```